Letterhead and Envelope Design for Investment Company

We need a letterhead and envelope design.
We are a family owned investment company doing direct investments into other family owned businesses.
I have attached all our current marketing material including our logo for reference.

Our under construction website can be found here:
https://rob-darke-qv7m.pagevorlo.com/
password: Copperfen

Target Market(s)

Bankers, business owners, financial partners

Industry/Entity Type

Investment

Colors

Designer to choose colors to be used in the design.

Requirements
Must have
• Logo, and company information

```html
<!DOCTYPE html>
<html lang="en">
<head>
<meta charset="utf-8">
<title>Copperfen Holdings – Letterhead and Envelope</title>
<link href="https://fonts.googleapis.com/css2?family=Raleway:wght@400;500;600&display=swap" rel="stylesheet">
<style>
  :root {
    --backdrop: #e4e4e4;
    --paper: #ffffff;
    --gold: #e3b024;
    --copper: #c86826;
    --ink: #2b2b2b;
    --muted: #8a8a8a;
    --ghost: #f1ebdd;
  }
  * { box-sizing: border-box; margin: 0; padding: 0; }
  html, body { width: 1200px; height: 927px; overflow: hidden; }
  body {
    background: var(--backdrop);
    font-family: "Raleway", sans-serif;
    position: relative;
  }
  .sheet {
    position: absolute;
    background: var(--paper);
    box-shadow: 0 6px 18px rgba(0,0,0,.18);
    overflow: hidden;
  }
  .letterhead { left: 60px; top: 70px; width: 600px; height: 776px; }
  .envelope { left: 690px; top: 440px; width: 480px; height: 208px; }

  .brand-name {
    position: absolute;
    color: var(--ink);
    font-weight: 500;
    letter-spacing: .08em;
    text-transform: uppercase;
    line-height: 1;
    display: flex;
    align-items: center;
    gap: 8px;
    white-space: nowrap;
  }
  .brand-dot { width: 9px; height: 9px; border-radius: 50%; background: var(--gold); flex: none; }
  .letterhead .brand-name { left: 44px; top: 52px; font-size: 15px; }
  .envelope .brand-name { left: 28px; top: 26px; font-size: 13px; }

  .watermark {
    position: absolute;
    color: var(--ghost);
    font-weight: 500;
    letter-spacing: .06em;
    text-transform: uppercase;
    white-space: nowrap;
    line-height: 1.15;
  }
  .letterhead .watermark { left: 0; right: 0; top: 330px; font-size: 36px; text-align: center; }
  .envelope .watermark { right: 22px; top: 128px; font-size: 15px; text-align: right; }

  .contact { position: absolute; font-size: 9px; color: var(--muted); line-height: 1.55; font-style: normal; white-space: nowrap; }
  .letterhead .contact { right: 36px; top: 132px; }
  .envelope .contact { left: 28px; top: 60px; font-size: 8.5px; }
  .contact-company { color: var(--copper); font-weight: 600; font-size: 10px; margin-bottom: 3px; }
  .contact-row { display: flex; align-items: center; gap: 6px; }
  .contact-row svg { width: 9px; height: 9px; flex: none; }

  .footer-band { position: absolute; left: 0; bottom: 0; width: 100%; }
  .letterhead .footer-band { height: 66px; }
  .envelope .footer-band { height: 34px; }
</style>
</head>
<body>

<section class="sheet letterhead">
  <div class="brand-name"><span class="brand-dot"></span>Copperfen Holdings Inc</div>

  <address class="contact">
    <div class="contact-company">Copperfen Holdings, Inc</div>
    <div class="contact-row"><svg viewBox="0 0 10 10"><path d="M5 0.5a3.2 3.2 0 0 0-3.2 3.2C1.8 6 5 9.5 5 9.5S8.2 6 8.2 3.7A3.2 3.2 0 0 0 5 .5z" fill="#c86826"/></svg>418 Mill Row NE, Suite 210, Fenwick, IA 52890</div>
    <div class="contact-row"><svg viewBox="0 0 10 10"><circle cx="5" cy="5" r="4.3" fill="none" stroke="#c86826"/><path d="M3.4 3c.3 1.8 1.7 3.3 3.5 3.7" stroke="#c86826" fill="none"/></svg>319-555-0182</div>
    <div class="contact-row"><svg viewBox="0 0 10 10"><circle cx="5" cy="5" r="4.3" fill="none" stroke="#c86826"/><path d="M.7 5h8.6M5 .7v8.6" stroke="#c86826"/></svg>www.copperfenholdings.com</div>
    <div class="contact-row"><svg viewBox="0 0 10 10"><circle cx="5" cy="5" r="4.3" fill="none" stroke="#c86826"/><rect x="2.6" y="3.4" width="4.8" height="3.2" fill="none" stroke="#c86826" stroke-width=".8"/></svg>inquiries@copperfenholdings.com</div>
  </address>

  <div class="watermark">Copperfen Holdings<br>Inc</div>

  <svg class="footer-band" viewBox="0 0 600 66" preserveAspectRatio="none">
    <polygon points="0,0 58,0 22,66 0,66" fill="#e3b024"/>
    <polygon points="70,0 600,0 600,66 34,66" fill="#c86826"/>
  </svg>
</section>

<section class="sheet envelope">
  <div class="brand-name"><span class="brand-dot"></span>Copperfen Holdings Inc</div>

  <address class="contact">
    <div class="contact-company">Copperfen Holdings, Inc</div>
    <div class="contact-row"><svg viewBox="0 0 10 10"><path d="M5 0.5a3.2 3.2 0 0 0-3.2 3.2C1.8 6 5 9.5 5 9.5S8.2 6 8.2 3.7A3.2 3.2 0 0 0 5 .5z" fill="#c86826"/></svg>418 Mill Row NE, Suite 210, Fenwick, IA 52890</div>
    <div class="contact-row"><svg viewBox="0 0 10 10"><circle cx="5" cy="5" r="4.3" fill="none" stroke="#c86826"/><path d="M3.4 3c.3 1.8 1.7 3.3 3.5 3.7" stroke="#c86826" fill="none"/></svg>319-555-0182</div>
    <div class="contact-row"><svg viewBox="0 0 10 10"><circle cx="5" cy="5" r="4.3" fill="none" stroke="#c86826"/><path d="M.7 5h8.6M5 .7v8.6" stroke="#c86826"/></svg>www.copperfenholdings.com</div>
    <div class="contact-row"><svg viewBox="0 0 10 10"><circle cx="5" cy="5" r="4.3" fill="none" stroke="#c86826"/><rect x="2.6" y="3.4" width="4.8" height="3.2" fill="none" stroke="#c86826" stroke-width=".8"/></svg>inquiries@copperfenholdings.com</div>
  </address>

  <div class="watermark">Copperfen Holdings<br>Inc</div>

  <svg class="footer-band" viewBox="0 0 480 34" preserveAspectRatio="none">
    <polygon points="0,0 44,0 26,34 0,34" fill="#e3b024"/>
    <polygon points="52,0 480,0 480,34 34,34" fill="#c86826"/>
  </svg>
</section>

</body>
</html>
```